Optometrist/Eye Care Clinic Business card with new logo attached

We are a small, independent eye care clinic in Canada. We have recently updated our logo (as attached), and would like a professional, modern and health care oriented business card to highlight our office details and our optometrist. We'd like to incorporate the blue colours as seen on our logo.

Target Market(s)

demographic: age 35-65 male/female equal

Industry/Entity Type

Health Care

Contact Information for Business Card

Name of clinic: "Marrow Bend Eye Care Optometry"

Font styles to use
Sans Serif

Colors
0355a3

Requirements
Must have
• our website: marrowbendeyecare.com
• Dr Lena Quorvik
• Optometrist
• 217-392 E Halvering Ave
• Vancouver BC V6R 3J8
• P: 604-319-2058
• E: info@marrowbendeyecare.com
Nice to have
• front side: logo/name of clinic as seen on logo attached and website
• backside: logo on the left side, and name/title/address/phone/email

```html
<!DOCTYPE html>
<html lang="en">
<head>
<meta charset="utf-8">
<title>Marrow Bend Eye Care Optometry – Business Card</title>
<link rel="stylesheet" href="https://fonts.googleapis.com/css2?family=Roboto:wght@400;500;700&display=swap">
<style>
  :root {
    --brand-blue: #0355a3;
    --brand-teal: #1d7fb0;
    --ink-grey: #555b60;
    --card-white: #ffffff;
    --page-bg: #e9ebee;
  }
  * { box-sizing: border-box; margin: 0; padding: 0; }
  html, body { width: 1200px; height: 800px; overflow: hidden; }
  body {
    background: var(--page-bg);
    font-family: "Roboto", Arial, sans-serif;
    position: relative;
  }
  .card {
    position: absolute;
    width: 540px;
    height: 310px;
    background: var(--card-white);
    overflow: hidden;
    box-shadow: 0 2px 6px rgba(0,0,0,0.12);
  }
  .card--front { left: 40px; top: 245px; }
  .card--back  { left: 620px; top: 245px; }

  /* Front */
  .brand-lockup {
    position: absolute;
    left: 0; right: 0; top: 48px;
    display: flex; flex-direction: column; align-items: center;
  }
  .brand-mark {
    width: 70px; height: 70px; border-radius: 50%;
    background: var(--brand-blue);
    margin-bottom: 14px;
  }
  .brand-name {
    color: var(--brand-blue);
    font-weight: 400;
    font-size: 22px;
    letter-spacing: 3px;
    text-transform: uppercase;
    text-align: center;
    line-height: 1.25;
  }
  .stripe { position: absolute; left: 0; right: 0; background: var(--brand-blue); }
  .stripe--thin { top: 214px; height: 7px; }
  .stripe--tagline {
    top: 227px; height: 30px;
    color: var(--card-white);
    font-weight: 700; font-size: 13px;
    display: flex; align-items: center; justify-content: center;
  }
  .stripe--base { top: 263px; height: 20px; }

  /* Back */
  .back-shape { position: absolute; inset: 0; }
  .back-brand {
    position: absolute; left: 24px; top: 30px;
    display: flex; align-items: center; gap: 10px;
  }
  .back-brand .brand-mark { width: 40px; height: 40px; margin: 0; }
  .back-brand .brand-name { font-size: 13px; letter-spacing: 2px; text-align: left; }
  .person { position: absolute; left: 34px; top: 118px; }
  .person-name { color: var(--brand-teal); font-weight: 700; font-size: 18px; text-transform: uppercase; }
  .person-title { color: var(--ink-grey); font-weight: 500; font-size: 13px; margin-top: 3px; }
  .contact-list {
    position: absolute; left: 34px; top: 200px;
    list-style: none; color: var(--card-white); font-size: 13px;
  }
  .contact-list li { display: flex; align-items: center; gap: 14px; height: 23px; }
  .contact-list svg { width: 13px; height: 13px; fill: var(--card-white); flex: none; }
</style>
</head>
<body>

<section class="card card--front" aria-label="Business card front">
  <div class="brand-lockup">
    <span class="brand-mark" aria-hidden="true"></span>
    <p class="brand-name">Marrow Bend<br>Eye Care<br>Optometry</p>
  </div>
  <div class="stripe stripe--thin"></div>
  <div class="stripe stripe--tagline">"Marrow Bend Eye Care Optometry"</div>
  <div class="stripe stripe--base"></div>
</section>

<section class="card card--back" aria-label="Business card back">
  <svg class="back-shape" viewBox="0 0 540 310" preserveAspectRatio="none" aria-hidden="true">
    <path d="M0 180 L300 180 C320 180 330 172 340 150 L540 150 L540 310 L0 310 Z" fill="#0355a3"/>
  </svg>
  <div class="back-brand">
    <span class="brand-mark" aria-hidden="true"></span>
    <p class="brand-name">Marrow Bend<br>Eye Care Optometry</p>
  </div>
  <div class="person">
    <p class="person-name">Dr Lena Quorvik</p>
    <p class="person-title">Optometrist</p>
  </div>
  <ul class="contact-list">
    <li><svg viewBox="0 0 24 24"><path d="M6.6 10.8a15 15 0 0 0 6.6 6.6l2.2-2.2a1 1 0 0 1 1-.25 11.4 11.4 0 0 0 3.6.57 1 1 0 0 1 1 1V20a1 1 0 0 1-1 1A17 17 0 0 1 3 4a1 1 0 0 1 1-1h3.5a1 1 0 0 1 1 1c0 1.25.2 2.45.57 3.57a1 1 0 0 1-.25 1z"/></svg>604-319-2058</li>
    <li><svg viewBox="0 0 24 24"><path d="M2 5h20v14H2zM4 7v.4l8 5 8-5V7l-8 5z"/></svg>info@marrowbendeyecare.com</li>
    <li><svg viewBox="0 0 24 24"><path d="M12 2a10 10 0 1 0 0 20 10 10 0 0 0 0-20zm6.9 9h-3a15 15 0 0 0-1.3-5.6A8 8 0 0 1 18.9 11zM12 4c.9 1.2 1.8 3.6 1.9 7h-3.8c.1-3.4 1-5.8 1.9-7zM9.4 5.4A15 15 0 0 0 8.1 11h-3a8 8 0 0 1 4.3-5.6zM5.1 13h3a15 15 0 0 0 1.3 5.6A8 8 0 0 1 5.1 13zM12 20c-.9-1.2-1.8-3.6-1.9-7h3.8c-.1 3.4-1 5.8-1.9 7zm2.6-1.4a15 15 0 0 0 1.3-5.6h3a8 8 0 0 1-4.3 5.6z"/></svg>marrowbendeyecare.com</li>
    <li><svg viewBox="0 0 24 24"><path d="M12 2a7 7 0 0 0-7 7c0 5 7 13 7 13s7-8 7-13a7 7 0 0 0-7-7zm0 9.5A2.5 2.5 0 1 1 12 6.5a2.5 2.5 0 0 1 0 5z"/></svg>217-392 E Halvering Ave Vancouver BC V6R 3J8</li>
  </ul>
</section>

</body>
</html>
```